Board Presentation template

Design a simple and clean PowerPoint slide templates for a Board meeting. The slides should have predominantly white backgrounds and use the colors of our Logo (attached): Tones of grey and orange and blue.
The company name is called Harbor Lane Gauges.
It sell, calibrate, service and repair industrial and commercial scales of all types. In particular, Truck scales, floor scales, counting scales and benchtop scales.
There is no website for Harbor Lane Gauges, but we have three affiliates that have their own websites:
https://www.tallyloadworks.com/
https://northbendbalanceandmeasure.com/
https://kvbalance.com/
Target Market(s)
Industrial and Commercial Weighing systems
Industry/Entity Type
Look and feel
Each slider illustrates characteristics of the customer's brand and the style your logo design should communicate.

```html
<!DOCTYPE html>
<html lang="en">
<head>
<meta charset="utf-8">
<title>Harbor Lane Gauges — Board Meeting Deck 2025</title>
<link rel="stylesheet" href="https://fonts.googleapis.com/css2?family=Bebas+Neue&family=Poppins:wght@400;500;600;700&display=swap">
<style>
  :root {
    --red: #cf3e33;
    --ink: #1b1b1b;
    --navy: #2f5f88;
    --steel: #7f9bb3;
    --sky: #a9bfd1;
    --mist: #dfe6ec;
    --grey: #8f9296;
    --panel: #e9ebee;
    --white: #ffffff;
    --stage: #cacaca;
  }
  * { box-sizing: border-box; margin: 0; padding: 0; }
  html, body { width: 1200px; height: 801px; overflow: hidden; }
  body {
    background: var(--stage);
    font-family: "Poppins", sans-serif;
    color: var(--ink);
  }
  .deck {
    display: grid;
    grid-template-columns: repeat(3, 360px);
    grid-template-rows: repeat(3, 203px);
    gap: 48px 30px;
    padding: 48px 30px;
  }
  .slide {
    position: relative;
    width: 360px;
    height: 203px;
    background: var(--white);
    overflow: hidden;
    box-shadow: 0 6px 14px rgba(0,0,0,.18);
  }
  .slide--red { background: var(--red); }
  .slide--qa { grid-column: 2; }
  .abs { position: absolute; }
  .heading {
    font-family: "Bebas Neue", sans-serif;
    font-size: 24px;
    line-height: .95;
    letter-spacing: .5px;
    color: var(--ink);
  }
  .heading::after {
    content: ""; display: block; width: 34px; height: 2px;
    background: var(--navy); margin-top: 4px;
  }
  .brand-mini {
    position: absolute; top: 10px; right: 12px;
    display: flex; align-items: center; gap: 4px;
    font-size: 6px; font-weight: 600; color: var(--ink);
    text-transform: uppercase; letter-spacing: .3px;
  }
  .brand-mini i { width: 7px; height: 7px; border-radius: 50%; background: var(--ink); display: block; }
  .note { font-size: 5px; line-height: 1.3; color: #555; }
  .big-num { font-family: "Bebas Neue", sans-serif; line-height: 1; }
  .tagline { font-size: 6px; line-height: 1.25; }
  .tagline b { font-weight: 700; }

  /* title */
  .title-brand { left: 40px; top: 86px; display: flex; align-items: center; gap: 7px;
    font-size: 11px; font-weight: 700; color: var(--ink); text-transform: uppercase; line-height: 1.1; width: 120px; }
  .title-brand i { width: 14px; height: 14px; border-radius: 50%; background: var(--ink); flex: none; display: block; }
  .title-text { left: 178px; top: 62px; font-family: "Bebas Neue", sans-serif; font-size: 38px; line-height: .88; color: var(--white); }
  .title-text span { color: var(--ink); }

  /* priorities */
  .p-circle { position: absolute; border-radius: 50%; display: flex; flex-direction: column; align-items: center; justify-content: center; color: var(--white); font-family: "Bebas Neue", sans-serif; }
  .p-list { right: 0; top: 6px; width: 138px; }
  .p-item { display: flex; gap: 8px; padding: 8px 10px; }
  .p-item--on { background: var(--mist); }
  .p-item i { width: 12px; height: 12px; border-radius: 50%; border: 1px solid var(--steel); flex: none; display: block; margin-top: 2px; }
  .p-item h4 { font-size: 6px; font-weight: 700; }

  /* funding */
  .f-panel { right: 0; top: 0; width: 118px; height: 100%; background: var(--panel); }
  .f-row { left: 30px; display: flex; align-items: center; gap: 8px; }
  .f-row i { width: 18px; height: 18px; border-radius: 50%; border: 1px solid var(--grey); display: block; }
  .f-row .rule { width: 1px; height: 24px; background: var(--red); }
  .f-amt { font-family: "Bebas Neue", sans-serif; font-size: 22px; line-height: 1; }
  .f-amt small { font-size: 10px; }

  /* insight */
  .i-sub { display: flex; gap: 7px; align-items: center; margin-bottom: 9px; }
  .i-sub i { width: 17px; height: 17px; border-radius: 50%; display: block; flex: none; }
  .i-sub h4 { font-size: 6px; font-weight: 700; }

  /* finances */
  .fin-table { left: 40px; top: 60px; border-collapse: collapse; font-size: 5px; }
  .fin-table th { background: var(--steel); color: var(--white); font-weight: 600; padding: 4px 0; width: 58px; }
  .fin-table th.y2 { background: var(--navy); }
  .fin-table td { border-bottom: 1px solid #ccc; padding: 3px 4px; text-align: center; }
  .fin-table td.lbl { text-align: left; width: 90px; background: var(--mist); }

  /* q&a */
  .qa-mark { left: 118px; top: 48px; font-family: "Bebas Neue", sans-serif; font-size: 96px; line-height: 1; color: var(--white); }
  .qa-q { left: 188px; top: 18px; font-family: "Bebas Neue", sans-serif; font-size: 150px; line-height: 1; color: var(--ink); }
  .qa-label { left: 218px; top: 54px; font-family: "Bebas Neue", sans-serif; font-size: 15px; line-height: 1.05; color: var(--white); }
</style>
</head>
<body>
<main class="deck">

  <!-- title -->
  <section class="slide slide--red">
    <div class="abs title-brand"><i></i>Harbor Lane Gauges</div>
    <h1 class="abs title-text">Boardmeeting<br>Deck <span>2025</span></h1>
  </section>

  <!-- priorities -->
  <section class="slide">
    <h2 class="abs heading" style="left:22px;top:16px;">Current Priorities</h2>
    <div class="p-circle" style="left:112px;top:62px;width:58px;height:58px;background:var(--steel);font-size:18px;">80%</div>
    <div class="p-circle" style="left:96px;top:112px;width:50px;height:50px;background:var(--grey);font-size:16px;">20%</div>
    <div class="p-circle" style="left:40px;top:64px;width:76px;height:76px;background:var(--red);font-size:26px;">29K
      <span style="font-family:Poppins,sans-serif;font-size:4px;">Total scale calibrations</span></div>
    <div class="abs p-list">
      <div class="p-item"><i></i><div><h4>M. Goals</h4><p class="note">Short note on the key goal this year</p></div></div>
      <div class="p-item p-item--on"><i></i><div><h4>M. Objectives</h4><p class="note">Short note on the key goal this year</p></div></div>
      <div class="p-item"><i></i><div><h4>M. Tactics</h4><p class="note">Short note on the key goal this year</p></div></div>
    </div>
  </section>

  <!-- company at glance -->
  <section class="slide">
    <div class="brand-mini"><i></i>Harbor Lane Gauges</div>
    <h2 class="abs heading" style="left:22px;top:48px;">Company at Glance</h2>
    <div class="abs" style="left:22px;top:120px;">
      <div class="big-num" style="font-size:26px;color:var(--red);">2.10B</div>
      <p class="note" style="color:var(--red);">Total funding</p>
      <p class="tagline" style="margin-top:6px;"><b>Good Idea</b><br><b>Makes</b> Everything is Better</p>
    </div>
    <svg class="abs" style="left:170px;top:36px;" width="180" height="150" viewBox="0 0 180 150">
      <rect x="20" y="10" width="158" height="120" fill="var(--mist)" opacity=".5"/>
      <text x="22" y="8" font-size="5" font-family="Poppins" font-weight="600">GROWTH PLAN</text>
      <g font-size="5" font-family="Poppins" fill="#333">
        <text x="6" y="30">35</text><text x="6" y="60">25</text><text x="6" y="90">15</text><text x="6" y="125">0</text>
        <text x="30" y="140">Jan</text><text x="70" y="140">Feb</text><text x="110" y="140">Mar</text><text x="150" y="140">Apr</text>
      </g>
      <polyline fill="none" stroke="var(--navy)" stroke-width="1.2" points="22,85 40,85 52,75 66,78 80,62 96,58 110,48 124,42 140,56 152,30 166,20 176,25"/>
      <polyline fill="none" stroke="var(--steel)" stroke-width="1" stroke-dasharray="2 2" points="22,78 40,92 56,80 72,86 88,70 104,72 120,60 136,66 150,48 164,52 176,30"/>
    </svg>
  </section>

  <!-- insight -->
  <section class="slide">
    <div class="brand-mini"><i></i>Harbor Lane Gauges</div>
    <h2 class="abs heading" style="left:22px;top:16px;">Insight</h2>
    <svg class="abs" style="left:20px;top:72px;" width="90" height="120" viewBox="0 0 90 120">
      <rect x="4" y="30" width="9" height="80" rx="4" fill="var(--navy)"/>
      <rect x="18" y="20" width="9" height="90" rx="4" fill="var(--grey)"/>
      <rect x="32" y="55" width="9" height="55" rx="4" fill="var(--steel)"/>
      <rect x="46" y="10" width="9" height="100" rx="4" fill="var(--mist)"/>
      <rect x="60" y="40" width="9" height="70" rx="4" fill="var(--grey)"/>
      <g font-size="5" font-family="Poppins" fill="#555"><text x="4" y="119">Jan</text><text x="32" y="119">Feb</text><text x="58" y="119">Mar</text></g>
    </svg>
    <div class="abs" style="left:118px;top:58px;">
      <p class="tagline"><b>Good Idea</b><br><b>Makes</b> Everything<br>is Better</p>
      <div class="big-num" style="font-size:22px;color:var(--navy);margin-top:8px;">2.10B</div>
      <p class="note">Billion</p>
      <div class="big-num" style="font-size:22px;color:var(--sky);margin-top:4px;">1.09M</div>
      <p class="note">Million</p>
    </div>
    <div class="abs" style="left:190px;top:50px;width:1px;height:120px;background:#ddd;"></div>
    <div class="abs" style="left:202px;top:52px;width:140px;">
      <div class="i-sub"><i style="background:var(--steel);"></i><div><h4>Subtitle here</h4><p class="note">Short note on this point for the board</p></div></div>
      <div class="i-sub"><i style="background:var(--navy);"></i><div><h4>Subtitle Here</h4><p class="note">Short note on this point for the board</p></div></div>
      <div class="i-sub"><i style="background:var(--mist);"></i><div><h4>Subtitle Here</h4><p class="note">Short note on this point for the board</p></div></div>
    </div>
  </section>

  <!-- funding usage plan -->
  <section class="slide">
    <div class="abs f-panel"></div>
    <div class="brand-mini"><i></i>Harbor Lane Gauges</div>
    <h2 class="abs heading" style="left:30px;top:46px;">Funding<br>Usage Plan</h2>
    <div class="abs f-row" style="top:124px;"><i></i><span class="rule"></span>
      <div><div class="f-amt"><small>$</small>1.3<small>Billion</small></div><p class="note">Equipment and service fleet</p></div></div>
    <div class="abs f-row" style="top:160px;"><i></i><span class="rule" style="background:var(--navy);"></span>
      <div><div class="f-amt"><small>$</small>5.2<small>Million</small></div><p class="note">Operations and staff</p></div></div>
    <svg class="abs" style="left:190px;top:14px;" width="160" height="170" viewBox="0 0 160 170">
      <circle cx="80" cy="86" r="50" fill="none" stroke="var(--steel)" stroke-width="38"/>
      <circle cx="80" cy="86" r="50" fill="none" stroke="var(--sky)" stroke-width="38" stroke-dasharray="31.4 314.2" stroke-dashoffset="-94.2" transform="rotate(-90 80 86)"/>
      <path d="M80 86 L80 22 A64 64 0 0 1 143 100 Z" fill="var(--red)"/>
      <circle cx="80" cy="86" r="24" fill="var(--white)"/>
      <path d="M28 40 A74 74 0 0 0 42 150" fill="none" stroke="var(--navy)" stroke-width="1"/>
      <g font-family="Bebas Neue" fill="var(--white)">
        <text x="96" y="62" font-size="18">30%</text>
        <text x="32" y="108" font-size="16">60%</text>
        <text x="100" y="120" font-size="14" fill="var(--ink)">10%</text>
      </g>
    </svg>
  </section>

  <!-- finances -->
  <section class="slide">
    <div class="brand-mini"><i></i>Harbor Lane Gauges</div>
    <h2 class="abs heading" style="left:22px;top:22px;">Finances</h2>
    <table class="abs fin-table">
      <tr><th style="background:none;"></th><th>2026</th><th class="y2">2027</th></tr>
      <tr><td class="lbl">Revenue</td><td>$ 000.00</td><td>$ 000.00</td></tr>
      <tr><td class="lbl">Scale Sales</td><td>$ 000.00</td><td>$ 000.00</td></tr>
      <tr><td class="lbl">Field Service</td><td>$ 000.00</td><td>$ 000.00</td></tr>
      <tr><td class="lbl">Repairs</td><td>$ 000.00</td><td>$ 000.00</td></tr>
      <tr><td class="lbl">Calibration</td><td>$ 000.00</td><td>$ 000.00</td></tr>
    </table>
    <div class="abs" style="left:262px;top:64px;">
      <div class="big-num" style="font-size:26px;color:var(--red);">2.10B</div>
      <p class="note" style="color:var(--red);">Total funding</p>
      <p class="tagline" style="margin-top:6px;"><b>Good Idea</b><br><b>Makes</b> Everything is Better</p>
    </div>
  </section>

  <!-- q&a -->
  <section class="slide slide--red slide--qa">
    <div class="abs qa-mark">Q&amp;A</div>
    <div class="abs qa-q">?</div>
    <div class="abs qa-label">Question<br>And<br>Answer</div>
  </section>

</main>
</body>
</html>
```